Brightwire Hollow Business cards

one side I would like my logo (uploaded) and the other side I want my details. I'm an electrician in sydney. The logo side I'm happy with just a white background and our logo in the middle.

Details for other side
24/7 Sydney Electrician
Marcus Pell
0431 587 219
marcus@brightwirehollow.com.au
brightwirehollow.com.au
icons for facebook, instagram, linked in

Industry/Entity Type

electrician

Contact Information for Business Card

company info

```html
<!DOCTYPE html>
<html lang="en">
<head>
<meta charset="utf-8">
<title>Brightwire Hollow – Business Cards</title>
<link href="https://fonts.googleapis.com/css2?family=Michroma&display=swap" rel="stylesheet">
<style>
  :root {
    --backdrop: #b3b3b3;
    --paper: #ffffff;
    --ink: #0c0c0c;
    --accent: #e8322a;
    --light-text: #f4f4f4;
  }
  html, body {
    margin: 0;
    padding: 0;
    width: 1200px;
    height: 1200px;
    overflow: hidden;
    background: var(--backdrop);
    font-family: "Michroma", sans-serif;
  }
  .card {
    position: absolute;
    left: 260px;
    width: 681px;
    height: 456px;
  }
  .card--front { top: 109px; background: var(--paper); }
  .card--back  { top: 660px; background: var(--ink); color: var(--light-text); }

  .wordmark {
    position: absolute;
    left: 0;
    width: 100%;
    text-align: center;
    color: var(--accent);
    font-weight: 400;
    text-transform: uppercase;
    line-height: 1.15;
    margin: 0;
  }
  .card--front .wordmark { top: 176px; font-size: 36px; letter-spacing: 1px; }
  .card--back .wordmark  { top: 72px; font-size: 30px; letter-spacing: 1px; }

  .contact-name {
    position: absolute;
    top: 182px;
    width: 100%;
    text-align: center;
    font-size: 17px;
    letter-spacing: 1px;
    margin: 0;
  }
  .contact-list {
    position: absolute;
    top: 217px;
    width: 100%;
    margin: 0;
    padding: 0;
    list-style: none;
  }
  .contact-item {
    display: flex;
    justify-content: center;
    align-items: center;
    gap: 10px;
    height: 34px;
    font-size: 13px;
    letter-spacing: 1.2px;
  }
  .contact-item--phone { font-size: 16px; height: 36px; }
  .contact-item svg { flex: none; }

  .social-row {
    position: absolute;
    top: 333px;
    width: 100%;
    display: flex;
    justify-content: center;
    gap: 9px;
  }
  .social-dot {
    width: 18px;
    height: 18px;
    border-radius: 50%;
    background: var(--accent);
  }

  .rule {
    position: absolute;
    left: 22px;
    width: 636px;
    height: 9px;
    background: var(--accent);
  }
  .rule--upper { top: 373px; }
  .rule--lower { top: 400px; }
  .tagline {
    position: absolute;
    top: 366px;
    left: 183px;
    width: 313px;
    height: 25px;
    background: var(--accent);
    color: var(--light-text);
    font-size: 11px;
    letter-spacing: 4px;
    display: flex;
    align-items: center;
    justify-content: center;
    text-transform: uppercase;
    margin: 0;
  }
</style>
</head>
<body>
  <section class="card card--front">
    <p class="wordmark">Brightwire<br>Hollow</p>
  </section>

  <section class="card card--back">
    <p class="wordmark">Brightwire<br>Hollow</p>
    <p class="contact-name">Marcus Pell</p>
    <ul class="contact-list">
      <li class="contact-item contact-item--phone">
        <svg width="16" height="17" viewBox="0 0 24 24" aria-hidden="true"><path fill="#e8322a" d="M6.6 10.8a15 15 0 0 0 6.6 6.6l2.2-2.2a1 1 0 0 1 1-.25 11.4 11.4 0 0 0 3.6.6 1 1 0 0 1 1 1V20a1 1 0 0 1-1 1A17 17 0 0 1 3 4a1 1 0 0 1 1-1h3.5a1 1 0 0 1 1 1c0 1.25.2 2.45.6 3.6a1 1 0 0 1-.25 1z"/></svg>
        <span>0431 587 219</span>
      </li>
      <li class="contact-item">
        <svg width="18" height="12" viewBox="0 0 18 12" aria-hidden="true"><rect width="18" height="12" fill="#e8322a"/><path d="M0.5 0.5 9 7 17.5 0.5M0.5 11.5 6.5 5.5M17.5 11.5 11.5 5.5" stroke="#0c0c0c" stroke-width="0.9" fill="none"/></svg>
        <span>marcus@brightwirehollow.com.au</span>
      </li>
      <li class="contact-item">
        <svg width="15" height="15" viewBox="0 0 24 24" aria-hidden="true"><circle cx="12" cy="12" r="11" fill="#e8322a"/><path d="M1 12h22M12 1c-4 4-4 18 0 22M12 1c4 4 4 18 0 22" stroke="#0c0c0c" stroke-width="1.6" fill="none"/></svg>
        <span>brightwirehollow.com.au</span>
      </li>
    </ul>
    <div class="social-row">
      <span class="social-dot"></span>
      <span class="social-dot"></span>
      <span class="social-dot"></span>
    </div>
    <div class="rule rule--upper"></div>
    <div class="rule rule--lower"></div>
    <p class="tagline">24/7 Sydney Electrician</p>
  </section>
</body>
</html>
```